Marketing brochure for Ferncrest Staffing Solutions

We need a marketing brochure for potential clients to showcase our services and benefits. We are after a 4 page A4 brochure that can be printed and also sent electronically. I have attached some one page flyers we use for branding purposes as well as images that may be used (feel free to use others).

Also attached is the copy and flowhart image.

We want this brochure to look professional and communicate an honest business.

```html
<!DOCTYPE html>
<html lang="en">
<head>
<meta charset="utf-8">
<title>Ferncrest Staffing Solutions – Brochure</title>
<link rel="stylesheet" href="https://fonts.googleapis.com/css2?family=Poppins:wght@400;500;600;700;800&display=swap">
<style>
:root{
  --navy:#0f2a6e;
  --brand:#1b4e95;
  --deep:#1a4a86;
  --cyan:#16c0e4;
  --sky:#27a2ea;
  --grey:#c9ccd3;
  --ink:#222;
  --white:#fff;
}
*{margin:0;padding:0;box-sizing:border-box}
html,body{width:873px;height:1200px;overflow:hidden;background:var(--white)}
body{position:relative;font-family:"Poppins",sans-serif;color:var(--ink)}
.page{position:absolute;width:328px;height:463px;overflow:hidden;background:var(--white);box-shadow:0 3px 12px rgba(0,0,0,.18)}
.page--cover{left:79px;top:87px}
.page--intro{left:467px;top:87px}
.page--process{left:73px;top:630px}
.page--contact{left:471px;top:630px;background:var(--deep)}
.abs{position:absolute}
.small{font-size:4.3px;line-height:1.35}

/* cover */
.dots{left:150px;top:0;width:178px;height:300px;background:radial-gradient(ellipse at 100% 0%,#d8d8d8 0%,#ececec 40%,rgba(255,255,255,0) 75%)}
.brand-lockup{display:flex;align-items:center;gap:5px}
.brand-lockup .mark{width:36px;height:36px;border-radius:50%;background:var(--brand)}
.brand-lockup .name{font-weight:700;font-size:8px;line-height:1.15;color:var(--brand)}
.cover-ring{left:36px;top:67px;width:246px;height:246px;border-radius:50%;background:var(--navy)}
.cover-white{left:69px;top:100px;width:180px;height:180px;border-radius:50%;background:var(--white)}
.cover-photo{left:79px;top:110px;width:160px;height:160px;border-radius:50%;background:linear-gradient(180deg,#7fb3dc 0%,#9cc6e6 40%,#3b3f4a 75%,#23262d 100%)}
.welcome{left:25px;top:335px;font-size:15px;font-weight:600;letter-spacing:3px;color:#111}
.cover-title{left:24px;top:352px;font-size:37px;font-weight:800;line-height:1;color:var(--brand);letter-spacing:-.5px}
.cover-sub{left:25px;top:393px;font-size:17px;font-weight:700;color:var(--brand)}
.cover-url{left:24px;top:427px;font-size:10px;font-weight:500;letter-spacing:1.5px;color:#111}

/* intro */
.h2{font-size:9.5px;font-weight:800;line-height:1.05;color:var(--brand)}
.intro-ring{left:198px;top:-5px;width:200px;height:200px;border-radius:50%;background:var(--navy)}
.intro-white{left:222px;top:13px;width:158px;height:158px;border-radius:50%;background:var(--white)}
.intro-photo{left:227px;top:18px;width:148px;height:148px;border-radius:50%;background:linear-gradient(160deg,#c9d6e3 0%,#8ea3b8 40%,#2f3a4c 100%)}
.benefit{left:20px;width:288px}
.bar{display:flex;align-items:center;height:10px;background:var(--grey);border-radius:0 5px 5px 0;position:relative}
.bar .num{width:15px;height:12px;margin-top:-2px;background:var(--brand);color:#fff;font-size:6.5px;font-weight:700;display:flex;align-items:center;justify-content:center}
.bar .label{font-size:5px;font-weight:700;margin-left:4px;color:#111}
.bar .icon{position:absolute;right:-1px;top:-1px;width:11px;height:11px;border-radius:50%;background:var(--brand);border:1.5px solid #fff}
.benefit p{margin-top:3px}
.footer{display:flex;align-items:center;width:288px;border-bottom:.6px solid var(--brand)}
.footer .url{background:var(--brand);color:#fff;font-size:4.5px;letter-spacing:1px;padding:1px 8px 1px 5px;clip-path:polygon(0 0,90% 0,100% 100%,0 100%)}
.footer .pg{margin-left:auto;width:5px;height:5px;border-radius:50%;background:var(--brand);color:#fff;font-size:3px;text-align:center;line-height:5px}

/* process */
.steps-top,.steps-bottom{left:16px;width:300px;display:flex}
.step{flex:1;text-align:center;font-size:4.6px;line-height:1.2;color:#333}
.step .ic{width:14px;height:14px;border-radius:50%;background:var(--navy);margin:0 auto 3px}
.steps-bottom .step .ic{margin:3px auto 0}
.process-lower{left:0;top:227px;width:328px;height:236px;background:linear-gradient(180deg,#1c4f8d 0%,#1a4a86 60%,#163e72 100%)}
.train-ring{left:177px;top:-5px;width:200px;height:200px;border-radius:50%;background:#3d8ed0}
.train-white{left:200px;top:18px;width:154px;height:154px;border-radius:50%;background:var(--white)}
.train-photo{left:204px;top:22px;width:146px;height:146px;border-radius:50%;background:linear-gradient(160deg,#e6ecf2 0%,#b8c4d0 45%,#2b3240 100%)}
.h2--light{color:#c7d3e4}
.lower-text{color:#fff}
.week{display:flex;align-items:center;gap:4px}
.week .tag{background:var(--cyan);color:#0d2a55;font-size:5.5px;font-weight:700;padding:1px 3px}
.footer--light{border-bottom-color:#9fc3ea}
.footer--light .url{background:var(--cyan);color:#0d2a55}

/* contact */
.skyline{inset:0;background:linear-gradient(180deg,#1e5191 0%,#1d4f8c 35%,#3a6aa2 62%,#1b4a85 82%,#1a4784 100%)}
.contact-brand .mark{width:60px;height:60px;background:#fff;opacity:.95}
.contact-brand .name{color:#fff;font-size:10px}
.more{left:0;width:328px;text-align:center;color:#fff}
.more h3{font-size:10px;font-weight:700}
.rule{left:20px;width:288px;height:.7px;background:#d7e3f2}
.director{color:#fff}
.director .nm{font-size:10px;font-weight:700}
.director .ln{font-size:6px;line-height:1.5}
.divider{left:163px;top:343px;width:.7px;height:28px;background:#d7e3f2}
.quote{left:32px;top:390px;width:270px;text-align:center;color:#fff;font-size:6.6px;line-height:1.25}
.qmark{font-size:20px;font-weight:800;color:#fff;line-height:1}
</style>
</head>
<body>

<!-- Page 1: cover -->
<section class="page page--cover">
  <div class="abs dots" role="img" aria-label="Soft halftone dot texture fading into the page"></div>
  <div class="abs brand-lockup" style="left:24px;top:28px">
    <span class="mark"></span>
    <span class="name">Ferncrest<br>Staffing Solutions</span>
  </div>
  <div class="abs cover-ring"></div>
  <div class="abs cover-white"></div>
  <div class="abs cover-photo" role="img" aria-label="Photo of three business professionals standing in front of a glass office building"></div>
  <div class="abs welcome">WELCOME TO</div>
  <div class="abs cover-title">FERNCREST</div>
  <div class="abs cover-sub">STAFFING SOLUTIONS</div>
  <div class="abs cover-url">www.ferncreststaffing.com.au</div>
</section>

<!-- Page 2: introduction and advantages -->
<section class="page page--intro">
  <div class="abs intro-ring"></div>
  <div class="abs intro-white"></div>
  <div class="abs intro-photo" role="img" aria-label="Photo of a team working together around a laptop in an office"></div>

  <h2 class="abs h2" style="left:20px;top:19px">INTRODUCING FERNCREST<br>STAFFING SOLUTIONS</h2>
  <div class="abs small" style="left:20px;top:44px;width:172px">
    <p>Ferncrest Staffing Solutions is an Australian based Recruitment and Immigration company with a key focus on job placing internationally skilled and experienced workers across multiple industries. We address current overwhelming skill shortages, specialising in occupations within the building and construction, hospitality and care sectors.</p>
    <p style="margin-top:5px">With our global networks, Ferncrest Staffing Solutions support onshore clients with commercially focused solutions to source appropriately qualified workers and assist them to obtain work and training visas efficiently.</p>
  </div>

  <h2 class="abs h2" style="left:20px;top:109px">THE ADVANTAGES OF EMPLOYING<br>FOREIGN WORKERS IN AUSTRALIA</h2>
  <p class="abs small" style="left:20px;top:136px;width:190px">As businesses strive for growth and success in an increasingly globalised world, the utilisation of a diverse and skilled workforce becomes imperative. Hiring internationally skilled workers in Australia can offer a myriad of advantages, bringing fresh perspectives, specialised skills, and cultural diversity to the workplace. There are numerous key benefits of employing foreign workers, which can be a game-changer for businesses looking to thrive in the competitive Australian market.</p>

  <div class="abs benefit" style="top:186px">
    <div class="bar"><span class="num">1</span><span class="label">ACCESS TO A DIVERSE TALENT POOL</span><span class="icon"></span></div>
    <p class="small">Australia is renowned for its multicultural society, and by employing foreign workers, businesses can tap into a vast talent pool with diverse backgrounds, experiences, problem-solving approaches, and skills. This diversity allows businesses to cater to a broader range of customers and clients, better understanding and meeting their needs.</p>
  </div>
  <div class="abs benefit" style="top:225px">
    <div class="bar"><span class="num">2</span><span class="label">FILLING SKILL GAPS</span><span class="icon"></span></div>
    <p class="small">Certain industries in Australia face skill shortages that hinder their growth and productivity. Hiring international workers with specialised skills and expertise bridges these gaps efficiently. Whether it's in the building and construction, healthcare, engineering, or hospitality sectors, workers bring valuable knowledge and qualifications that are locally in demand.</p>
  </div>
  <div class="abs benefit" style="top:264px">
    <div class="bar"><span class="num">3</span><span class="label">CREATE BETTER BUSINESS MARGINS</span><span class="icon"></span></div>
    <p class="small">In some cases, internationally skilled workers are willing to work for award wages compared to their Australian counterparts. This can result in cost savings for employers, especially in industries where labour costs make up a significant portion of the overall expenses.</p>
  </div>
  <div class="abs benefit" style="top:307px">
    <div class="bar"><span class="num">4</span><span class="label">GLOBAL MARKET INSIGHTS</span><span class="icon"></span></div>
    <p class="small">In some cases, internationally skilled workers are willing to work for award wages compared to their Australian counterparts. This can result in cost savings for employers, especially in industries where labour costs make up a significant portion of the overall expenses.</p>
  </div>
  <div class="abs benefit" style="top:349px">
    <div class="bar"><span class="num">5</span><span class="label">FOSTERING CULTURAL UNDERSTANDING</span><span class="icon"></span></div>
    <p class="small">Bringing international workers into the workforce can lead to greater cultural understanding and acceptance among employees. Exposure to different cultures can break down stereotypes, promote empathy, and create a more harmonious work environment. Such an environment often boosts employee morale and leads to higher retention rates.</p>
  </div>
  <div class="abs benefit" style="top:392px">
    <div class="bar"><span class="num">6</span><span class="label">INCREASE WORKER RETENTION AND LOYALTY</span><span class="icon"></span></div>
    <p class="small">International workers under sponsorship arrangements have an obligation to work only for their sponsoring employer for the duration of their visa. Additionally, international workers who have been supported by their employer to come to Australia from our source countries will have an increased level of loyalty and commitment. Hiring international workers increases worker and skill retention and creates a dedicated workforce for your business.</p>
  </div>
  <div class="abs footer" style="left:20px;top:440px"><span class="url">www.ferncreststaffing.com.au</span><span class="pg">1</span></div>
</section>

<!-- Page 3: visa pathways and training -->
<section class="page page--process">
  <h2 class="abs h2" style="left:20px;top:20px">VISA PATHWAYS</h2>
  <p class="abs small" style="left:19px;top:37px;width:292px">There are several pathways available to Australian companies wishing to employee skilled international workers. Our team of experts will identify the systematic approach most suitable for each client for a seamless and successful outcome. We partner with clients from the initial comprehensive needs analysis, assisting with the immigration processes and right through to work commencement.</p>
  <p class="abs small" style="left:19px;top:70px">Summary of the process is below.</p>

  <div class="abs steps-top" style="top:78px">
    <div class="step"><div class="ic"></div>Initial meeting<br>to identify needs</div>
    <div class="step"><div class="ic"></div>Review candidate<br>resumes</div>
    <div class="step"><div class="ic"></div>Select<br>candidates</div>
    <div class="step"><div class="ic"></div>Apply for candidates<br>Nomination</div>
    <div class="step"><div class="ic"></div>Candidates arrive<br>in Australia</div>
    <div class="step"><div class="ic"></div>Candidates<br>commence work</div>
  </div>

  <svg class="abs" style="left:14px;top:111px" width="300" height="68" viewBox="0 0 300 68" aria-hidden="true">
    <rect x="0" y="26" width="296" height="14" fill="#1a9fd9"/>
    <g>
      <path d="M22 40V14h-7l12-12 12 12h-7v26z" fill="#27a2ea"/>
      <path d="M73 40V14h-7l12-12 12 12h-7v26z" fill="#123f78"/>
      <path d="M124 40V14h-7l12-12 12 12h-7v26z" fill="#27a2ea"/>
      <path d="M175 40V14h-7l12-12 12 12h-7v26z" fill="#16c0e4"/>
      <path d="M226 40V14h-7l12-12 12 12h-7v26z" fill="#123f78"/>
      <path d="M277 40V14h-7l12-12 12 12h-7v26z" fill="#27a2ea"/>
    </g>
    <g>
      <path d="M47 26v26h-7l12 12 12-12h-7V26z" fill="#27a2ea"/>
      <path d="M98 26v26h-7l12 12 12-12h-7V26z" fill="#16c0e4"/>
      <path d="M149 26v26h-7l12 12 12-12h-7V26z" fill="#123f78"/>
      <path d="M200 26v26h-7l12 12 12-12h-7V26z" fill="#27a2ea"/>
      <path d="M251 26v26h-7l12 12 12-12h-7V26z" fill="#16c0e4"/>
    </g>
  </svg>

  <div class="abs steps-bottom" style="top:182px;left:40px;width:256px">
    <div class="step">Agreement/Requisition<br>Request completed<div class="ic"></div></div>
    <div class="step">Sponsorship application<br>(Dep. Home Affairs)<div class="ic"></div></div>
    <div class="step">Offer<br>positions<div class="ic"></div></div>
    <div class="step">Candidates<br>apply for Visa<br>(Dep. Home Affairs)<div class="ic"></div></div>
    <div class="step">Ferncrest onboards<br>candidates for work<br>in Australia<div class="ic"></div></div>
  </div>

  <div class="abs process-lower">
    <div class="abs train-ring"></div>
    <div class="abs train-white"></div>
    <div class="abs train-photo" role="img" aria-label="Photo of a trainer presenting to a group in a meeting room"></div>
    <h2 class="abs h2 h2--light" style="left:20px;top:18px">TRAINING</h2>
    <div class="abs small lower-text" style="left:20px;top:34px;width:145px">
      <p>We strive to connect talented individuals from around the world with reputable organisations in Australia. To facilitate an efficient transition into their new Australian workplace, we ensure our candidates are job ready through the completion of one of our Offshore Training Programs.</p>
      <p style="margin-top:7px">Our programs are eight (8) weeks of workplace focused training, delivered online and via video conferencing prior to arrive in Australia.</p>
      <div class="week" style="margin-top:10px"><span class="tag">Weeks 1 to 6</span><span>Australian workplace skills and language<br>for the specific sector.</span></div>
      <div class="week" style="margin-top:7px"><span class="tag">Weeks 7 &amp; 8</span><span>Role specific skills and language.</span></div>
      <p style="margin-top:12px">Completion of this training program as well as our extensive recruitment selection process, provide our clients the knowledge they are recruiting high calibre and reliable candidates who will transition seamlessly into their positions.</p>
    </div>
    <div class="abs footer footer--light" style="left:20px;top:214px"><span class="url">www.ferncreststaffing.com.au</span><span class="pg">2</span></div>
  </div>
</section>

<!-- Page 4: contact -->
<section class="page page--contact">
  <div class="abs skyline" role="img" aria-label="Faded blue-tinted photo of a city skyline"></div>
  <div class="abs brand-lockup contact-brand" style="left:104px;top:33px">
    <span class="mark" style="border-radius:50%"></span>
    <span class="name">Ferncrest<br>Staffing Solutions</span>
  </div>
  <div class="abs more" style="top:298px">
    <h3>MORE INFORMATION</h3>
    <p style="font-size:4.6px;line-height:1.3;margin:5px auto 0;width:250px">Find further information about how Ferncrest Staffing Solutions can help you with your recruitment needs please visit our website www.ferncreststaffing.com.au or contact one of our Directors below.</p>
  </div>
  <div class="abs rule" style="top:336px"></div>
  <div class="abs director" style="left:60px;top:341px">
    <div class="nm">Daniel Ashby</div>
    <div class="ln">✉ daniel@ferncreststaffing.com.au<br>☎ +61 400 123 456</div>
  </div>
  <div class="abs divider"></div>
  <div class="abs director" style="left:186px;top:341px">
    <div class="nm">Priya Lennox</div>
    <div class="ln">✉ priya@ferncreststaffing.com.au<br>☎ +61 400 654 321</div>
  </div>
  <div class="abs rule" style="top:385px"></div>
  <div class="abs qmark" style="left:22px;top:388px">“</div>
  <p class="abs quote">Builders Council estimates that workforce growth and replacement in the four years to November 2026 will mean the industry needs to attract around half a million workers.</p>
  <div class="abs qmark" style="left:290px;top:412px">”</div>
</section>

</body>
</html>
```